Business card design incorporating discount offer

We are a trade services company and we need a double sided business card that is going to be used by our tradesmen to give to customers on completion of their jobs.

Below are the key elements of the card that we would like to include:

-Main logo with text 'Expert Property Care' underneath.
-Up to 12 smaller icon logos with text 'Your local all-trade experts' to emphasise the point that we cover all the trades
-Discount offer - 10% discount
-Telephone number and website address
-Blank space for tradesman to enter his/her name
-Request for customer feedback with feedback url

This business card will be printed on regular card. In the past we have favoured designs that use a black background but we're open to new ideas.

I have attached a few files:

-A simple wire frame example to show how this card could look with the different elements mentioned above, feel free to use a layout similar to this or come up with something totally different (biz-card.pdf)
-Front and back of a loyalty card the we've used in the past (this card was printed on plastic)
-Front and back of a key fob design that we've previously used (this card was printed on plastic)
-A logo file with the 12 small icons and the main logo image

If you need further images or information please ask.

```html
<!DOCTYPE html>
<html lang="en">
<head>
<meta charset="utf-8">
<title>Norvale – Business Card</title>
<link href="https://fonts.googleapis.com/css2?family=Quicksand:wght@300;500;700&display=swap" rel="stylesheet">
<style>
  :root {
    --brand-blue: #0a7cc4;
    --brand-grey: #8e9095;
    --paper: #ffffff;
    --backdrop: #d9d9d9;
    --rule: #9cc9e8;
    --dots: #b5b5b5;
  }
  * { box-sizing: border-box; margin: 0; padding: 0; }
  html, body {
    width: 1200px; height: 1001px; overflow: hidden;
    background: var(--backdrop);
    font-family: "Quicksand", sans-serif;
  }
  .card {
    position: absolute; left: 200px;
    width: 800px; height: 420px;
    background: var(--paper);
    box-shadow: 0 6px 18px rgba(0,0,0,.18);
    overflow: hidden;
  }
  .card--back { top: 50px; }
  .card--front { top: 520px; }

  /* Back side */
  .icon-strip {
    position: absolute; left: 0; top: 0; bottom: 0; width: 240px;
    background: var(--brand-blue);
    display: grid; grid-template-columns: repeat(2, 66px);
    grid-auto-rows: 52px; gap: 10px 14px;
    justify-content: center; align-content: center;
  }
  .trade-icon { border-radius: 10px; box-shadow: inset 0 -4px 0 rgba(0,0,0,.15); }
  .back-content { position: absolute; left: 280px; right: 36px; top: 34px; color: var(--brand-blue); }
  .tagline { font-weight: 700; font-size: 33px; letter-spacing: .3px; }
  .tradesman-label { margin-top: 28px; font-weight: 700; font-size: 17px; }
  .write-line { margin: 22px 0 0 40px; border-bottom: 2px dotted var(--dots); }
  .write-line + .write-line { margin-top: 18px; }
  .divider { margin-top: 26px; border-top: 1px solid var(--rule); }
  .feedback-question { margin-top: 18px; font-weight: 700; font-size: 18px; }
  .feedback-button {
    margin: 14px 0 0 14px; padding: 10px 20px;
    background: var(--brand-blue); color: var(--paper);
    border-radius: 18px; text-align: center;
    font-weight: 500; font-size: 13px; letter-spacing: 1.6px; line-height: 1.45;
  }

  /* Front side */
  .brand-block { position: absolute; left: 60px; top: 70px; color: var(--brand-grey); }
  .brand-name { display: flex; align-items: center; gap: 18px; font-weight: 700; font-size: 84px; line-height: 1; }
  .brand-dot { width: 44px; height: 44px; border-radius: 50%; background: var(--brand-blue); }
  .brand-strap { margin-top: 30px; font-weight: 700; font-size: 38px; }
  .contact-list { position: absolute; left: 60px; top: 300px; list-style: none; color: var(--brand-grey); font-size: 19px; letter-spacing: 2px; }
  .contact-list li { display: flex; align-items: center; gap: 14px; margin-bottom: 12px; }
  .offer-panel {
    position: absolute; right: 0; top: 0; bottom: 0; width: 270px;
    background: var(--brand-blue); color: var(--paper); text-align: center;
  }
  .offer-percent { margin-top: 42px; font-weight: 300; font-size: 96px; line-height: 1; }
  .offer-word { font-weight: 300; font-size: 44px; line-height: 1; }
  .offer-note { font-weight: 300; font-size: 24px; letter-spacing: 2px; }
  .offer-small { position: absolute; bottom: 30px; left: 0; right: 0; font-weight: 300; font-size: 18px; line-height: 1.2; }
</style>
</head>
<body>

<section class="card card--back" aria-label="Card back">
  <div class="icon-strip" role="img" aria-label="Twelve trade icons: building, plumbing, decorating, pest control, cleaning, appliances, electrics, gas, carpentry, drainage, bathrooms, handyman">
    <span class="trade-icon" style="background:#2a8fd4"></span>
    <span class="trade-icon" style="background:#1f7fc4"></span>
    <span class="trade-icon" style="background:#d9313d"></span>
    <span class="trade-icon" style="background:#7bbf3a"></span>
    <span class="trade-icon" style="background:#f2c42c"></span>
    <span class="trade-icon" style="background:#3bb8a8"></span>
    <span class="trade-icon" style="background:#8a8d92"></span>
    <span class="trade-icon" style="background:#27a6e0"></span>
    <span class="trade-icon" style="background:#d9a021"></span>
    <span class="trade-icon" style="background:#6f7b89"></span>
    <span class="trade-icon" style="background:#a0308f"></span>
    <span class="trade-icon" style="background:#b77a45"></span>
  </div>
  <div class="back-content">
    <h2 class="tagline">Your local all-trade experts</h2>
    <p class="tradesman-label">Your Norvale tradesman:</p>
    <div class="write-line"></div>
    <div class="write-line"></div>
    <div class="divider"></div>
    <p class="feedback-question">What do you think about our service?</p>
    <p class="feedback-button">Leave your feedback online<br>www.norvale-trades.co.uk/feedback</p>
  </div>
</section>

<section class="card card--front" aria-label="Card front">
  <div class="brand-block">
    <div class="brand-name"><span class="brand-dot"></span>Norvale</div>
    <p class="brand-strap">Expert Property Care</p>
  </div>
  <ul class="contact-list">
    <li>
      <svg width="22" height="22" viewBox="0 0 22 22" aria-hidden="true">
        <circle cx="11" cy="11" r="10" fill="none" stroke="#0a7cc4" stroke-width="2"/>
        <path d="M8 6c-1 1-1 3 1 6s4 4 5 4l1-1-2-2-1 1c-1-.5-2-2-2.5-3l1-1-2-2z" fill="#0a7cc4"/>
      </svg>
      0800 123 4567
    </li>
    <li>
      <svg width="22" height="22" viewBox="0 0 22 22" aria-hidden="true">
        <circle cx="11" cy="11" r="10" fill="#0a7cc4"/>
        <g fill="none" stroke="#fff" stroke-width="1.2">
          <ellipse cx="11" cy="11" rx="4" ry="9"/>
          <line x1="2" y1="11" x2="20" y2="11"/>
          <line x1="4" y1="6.5" x2="18" y2="6.5"/>
          <line x1="4" y1="15.5" x2="18" y2="15.5"/>
        </g>
      </svg>
      www.norvale-trades.co.uk
    </li>
  </ul>
  <aside class="offer-panel">
    <p class="offer-percent">10%</p>
    <p class="offer-word">Discount</p>
    <p class="offer-note">with this card</p>
    <p class="offer-small">check our website for<br>full more details</p>
  </aside>
</section>

</body>
</html>
```